A unique communication angle to crowdfunding

Looking for a fresh redesign of a crowd funding website that deals in real estate. I already have the content, but am looking to take the design to the next level.

Existing real estate crowd funding sites focus on the real estate. I want to explore communication angle that:
- puts the investor in the centre of the communication: "become a baron"
- highlights the international nature (international properties, international investors)

There's also quite a lot of copy on the site, as we need to explain the service in quite a bit of detail. There's room to reduce the copy and replace with graphics. Could also consider clicking to see different text (see our difference section in http://galafeatherpost.com)

The backend of the platform is already being worked on by a specialist crowd funding service provider.

In total there are 5 pages to be designed.

The homepage is really important. Right now it looks quite dated. It doesn't have a great layout. Note there is no mobile version of the website, so the pages need to be seen well on mobile devices. When looking at the brief, refer to the following links too:

current website:
http://pebblemarquis.com

some revisions made so far:
http://preview.stackorchard.com/7K3JT9

Attached are logo files and another file which contained copy for the pages. No need to rework the logo.

Please make sure to use the same copy in the brief on the webpages, to ensure the layouts work. Designers are free to propose images they feel work on the pages.

I would like to see if rather than tweaking the pages, it's possible to come up with a better design concept. If the 5 pages are accepted, there's a chance I'll request an additional 4 pages.
Updates

Please note the font used in the logo is called "harabara" in case you decide to use it in any of the titles, etc.

Please note there is one additional page for which we would like to review designs. Note the page would be a template to be used on all future real estate detail pages. Here is an example of the current design for reference:

http://pebblemarquis.com/projects/view/14

In total there are 5 page designs required, (homepage + 4)

Thank you

FYI -

Just a quick note to give information from similar UK real estate crowdfunding sites:
http://www.tenantheron.co.uk
http://quaystone.co.uk
https://www.vaultmeridian.com

Of the above, only quaystone has a nice clean looking landing page. Information is clear and well laid out.

Hi all, just uploaded a new file in the brief. Contains some comments and a website reference. I thought it may help to explain how we could convey international aspect as well as how we could convey images in a more modern way. This is an option you can consider, but its entirely up to you how how answer the brief. Thanks!

We would like to let you know that we have just shortlisted the best designs. Together with that, we have also passed some detailed feedback to all designers who weren't shortlisted. If we didn't contact you, please let us know. If you haven't submitted a design or are working on revisions, please note these will no longer be taken into account now. We hope you understand that we need to close the project today. Thank you all once again for your great work and design concepts. Here's hoping we meet again on a future design brief. Cheers, pebblemarquis team.

Target Market(s)

At the moment, only rich are able to buy real estate. With this service, anyone can become a landlord. Target buyers:

Young professionals, looking to diversify from stock market and lower risk
People nearing retirement, looking for stable rental incomes
Retirees - looking to supplement pensions with possibility of capital gains
Parents - looking for a way to save long term for their children (instead of low interest paying bank accounts)

Industry/Entity Type

Communication

Font styles to use
Sans Serif
Other font styles liked:
• harabara

Colors
add136
f5f9eb
959595
000000

Requirements
Must have
• Overall, the site must convey "whoever you are, you too can become a landlord", and that you don't need to be wealthy to invest in real estate. See

Communication should put the investor (or the baron) at the centre. The investor can be any of those described in the target market.

Show the aspirational side of property ownership.

In addition to the investor/baron character, the second main theme is international. No other real estate crowdfunding website highlights this.
Nice to have
• Banner could show different consumer types, to illustrate that the service can appeal to many different profiles. Refer to attached file "home page reference - brightasdew.com" as an example of how this could be done.

Aim to show the international side of the service. Properties around the world, investors around the world.

```html
<!DOCTYPE html>
<html lang="en">
<head>
<meta charset="utf-8">
<title>pebblemarquis – Social real estate investment</title>
<link rel="stylesheet" href="https://fonts.googleapis.com/css2?family=Open+Sans:wght@400;600;700&display=swap">
<style>
:root{
  --green:#8cc63e;
  --green-dark:#74a92e;
  --green-pale:#f5f9eb;
  --ink:#2b2b2b;
  --text:#555555;
  --muted:#959595;
  --line:#dedede;
  --band:#f2f2f2;
  --dark:#3a3a3a;
  --darker:#2a2a2a;
  --white:#ffffff;
}
*{box-sizing:border-box;margin:0;padding:0}
html,body{width:1200px;height:3000px;overflow:hidden}
body{font-family:"Open Sans",Arial,sans-serif;color:var(--text);background:var(--white);position:relative}
a{color:inherit;text-decoration:none}
.green{color:var(--green);font-weight:600}

/* header */
.site-header{height:96px;position:relative;border-bottom:1px solid var(--line);background:var(--white)}
.brand{position:absolute;left:152px;top:28px}
.brand-name{font-size:26px;font-weight:600;color:var(--green);letter-spacing:-.3px}
.follow{position:absolute;left:618px;top:20px;display:flex;align-items:center;gap:8px;font-size:14px;color:var(--muted)}
.social-square{width:34px;height:28px;background:var(--green);display:block}
.social-square.alt{background:var(--muted)}
.search{position:absolute;left:808px;top:20px;width:246px;height:28px;display:flex}
.search-field{flex:1;background:#eeeeee;font-size:11px;color:#aaa;padding:7px 10px}
.search-btn{width:36px;background:#555;display:flex;align-items:center;justify-content:center}
.main-nav{position:absolute;right:144px;top:68px;display:flex;gap:22px;font-size:11px;font-weight:600;color:#666;text-transform:uppercase}
.main-nav a{padding-bottom:8px}
.main-nav a.current{color:var(--ink);border-bottom:2px solid var(--green)}

/* hero */
.hero{height:388px;position:relative;overflow:hidden}
.hero-photo{position:absolute;inset:0;background:linear-gradient(100deg,#eef0f2 0%,#dfe2e5 45%,#b8b39a 65%,#8f8a6e 80%,#6f7460 100%)}
.hero-caption{position:absolute;left:144px;top:152px;width:506px;height:80px;background:rgba(140,198,62,.92);padding:10px 20px;color:var(--white)}
.hero-caption h1{font-size:24px;font-weight:600;color:#1e2a10;line-height:1.2}
.hero-caption p{font-size:14px;margin-top:8px}
.hero-arrow{position:absolute;top:170px;width:42px;height:42px;border-radius:50%;background:#3b3b3b;display:flex;align-items:center;justify-content:center}
.hero-arrow.prev{left:96px}
.hero-arrow.next{left:1062px}
.hero-dots{position:absolute;left:130px;top:364px;display:flex;gap:4px}
.hero-dots span{width:10px;height:10px;border-radius:50%;background:#666}
.hero-dots span.on{background:var(--green)}

/* intro */
.intro{height:302px;text-align:center;padding-top:48px}
.section-title{font-size:28px;font-weight:600;color:var(--green);letter-spacing:-.3px}
.intro .rule{width:440px;height:1px;background:var(--line);margin:14px auto 18px}
.intro p{font-size:14px;line-height:22px;margin-bottom:22px;color:var(--text)}

/* actions */
.actions{height:306px;background:var(--band);border-top:1px solid var(--line);border-bottom:1px solid var(--line);display:flex;justify-content:center;gap:58px;padding-top:52px}
.action{width:368px}
.action-card{height:146px;background:var(--white);border:1px solid var(--line);display:flex;gap:22px;padding:26px 18px}
.action-icon{width:80px;height:80px;border-radius:50%;background:#3f3f3f;flex:none}
.action-card h2{font-size:20px;font-weight:600;color:var(--green);margin-bottom:6px}
.action-card p{font-size:13px;line-height:22px;color:var(--text)}
.action-btn{margin-top:14px;height:44px;background:var(--green);color:var(--white);font-size:19px;font-weight:700;display:flex;align-items:center;justify-content:center;box-shadow:0 4px 0 var(--green-dark);letter-spacing:-.3px}

/* projects */
.projects{height:622px;text-align:center;padding-top:28px}
.projects .section-title{font-size:22px}
.projects-lead{font-size:13px;line-height:24px;margin-top:14px;color:var(--text)}
.project-grid{display:flex;justify-content:center;gap:18px;margin-top:40px}
.project{width:292px;border:1px solid var(--line);text-align:left;background:var(--white)}
.project.raised{box-shadow:0 3px 8px rgba(0,0,0,.18)}
.project-photo{height:206px;position:relative}
.photo-a{background:linear-gradient(180deg,#7fb3e6 0%,#a9cbe9 40%,#8a5a44 60%,#9c8d7c 85%,#7a8a5a 100%)}
.photo-b{background:linear-gradient(180deg,#9fc6ec 0%,#c2d9ee 35%,#b9aa8e 55%,#c6bcaa 80%,#6f8d4a 100%)}
.photo-c{background:linear-gradient(180deg,#6fa8e0 0%,#a7cbe9 35%,#e6dccb 58%,#c89a6e 75%,#5f8a3f 100%)}
.price-tag{position:absolute;left:0;top:0;background:var(--green);color:var(--white);font-size:11px;font-weight:700;padding:4px 8px}
.launch-tag{position:absolute;left:0;top:26px;background:#5a7c2a;color:#e6f2d2;font-size:9px;font-weight:600;padding:3px 8px}
.project-body{padding:12px 14px 14px}
.project-body h3{font-size:14px;font-weight:600;color:var(--green);padding-bottom:8px;border-bottom:1px solid var(--line)}
.project-body p{font-size:11px;line-height:20px;margin-top:6px;color:var(--text);height:62px}
.funded{margin-top:8px;padding-top:8px;border-top:1px solid var(--line);font-size:12px;font-weight:600;color:#333}
.bar{height:18px;border:1px solid #cccccc;border-radius:3px;margin-top:4px;position:relative;background:#f4f4f4}
.bar-fill{height:100%;background:var(--green);border-radius:2px}
.bar-value{position:absolute;left:0;right:0;top:0;text-align:center;font-size:10px;line-height:16px;color:#333}
.project-link{display:block;text-align:center;font-size:13px;font-weight:600;color:var(--muted);margin-top:10px}
.project-link.active{color:var(--green)}

/* community */
.community{height:422px;position:relative;text-align:center;color:#cfcfcf;overflow:hidden}
.community-photo{position:absolute;inset:0;background:linear-gradient(180deg,#5a5a5a 0%,#4a4a4a 35%,#2f2f2f 70%,#1f1f1f 100%)}
.community-inner{position:relative;padding-top:50px}
.community .section-title{font-size:21px}
.community-lead{font-size:15px;line-height:24px;color:#9a9a9a;margin:12px auto 0;width:600px}
.stats{display:flex;justify-content:center;gap:66px;margin-top:40px}
.stat{width:260px;position:relative}
.stat-map{position:absolute;left:20px;top:-8px;width:220px;height:110px;border-radius:50%;background:radial-gradient(ellipse,rgba(140,198,62,.28),rgba(140,198,62,0) 70%)}
.stat-figure{position:relative;font-size:19px;font-weight:700;color:var(--green);line-height:24px;height:76px;display:flex;align-items:center;justify-content:center}
.stat-note{position:relative;font-size:15px;line-height:24px;color:#c8c8c8;margin-top:6px}

/* featured in */
.press{height:264px;position:relative}
.press-box{position:absolute;left:144px;top:60px;width:912px;height:194px;border:1px solid var(--line)}
.press-tag{position:absolute;left:522px;top:40px;width:176px;height:40px;background:var(--green);color:#1e2a10;font-size:17px;font-weight:600;display:flex;align-items:center;justify-content:center}
.press-row{position:absolute;left:0;right:0;display:flex;justify-content:center;align-items:center;gap:34px}
.press-row.first{top:60px}
.press-row.second{top:126px}
.press-badge{height:26px;background:#bdbdbd;border-radius:2px}
.press-badge.dark{background:#8a8a8a}

/* skyline */
.skyline{height:140px;background:linear-gradient(180deg,#ffffff 0%,#e4e4e4 40%,#a9a9a9 100%)}

/* footer */
.footer-bar{height:64px;background:var(--dark);display:flex;align-items:center;justify-content:space-between;padding:0 144px}
.footer-follow{display:flex;align-items:center;gap:12px;color:var(--green);font-size:17px;font-weight:600}
.footer-follow .social-outline{width:36px;height:28px;border:2px solid var(--green);display:block}
.copyright{color:var(--green);font-size:12px}
.site-footer{height:396px;background:#f7f7f7;padding:24px 144px 0;font-size:12.5px;line-height:21px;color:var(--text)}
.footer-top{display:flex;justify-content:space-between;align-items:flex-start;margin-bottom:20px}
.footer-top p{width:580px}
.group-name{font-size:20px;font-weight:600;color:#3a3a3a;line-height:28px;margin-top:10px;margin-right:48px}
.site-footer p.legal{margin-bottom:20px}
</style>
</head>
<body>

<header class="site-header">
  <a class="brand" href="#"><span class="brand-name">pebblemarquis</span></a>
  <div class="follow">Follow us on <span class="social-square"></span><span class="social-square alt"></span></div>
  <div class="search">
    <div class="search-field">Search...</div>
    <div class="search-btn"><svg width="14" height="14" viewBox="0 0 14 14"><circle cx="6" cy="6" r="4.5" fill="none" stroke="#fff" stroke-width="2"/><line x1="9.5" y1="9.5" x2="13" y2="13" stroke="#fff" stroke-width="2"/></svg></div>
  </div>
  <nav class="main-nav">
    <a class="current" href="#">Home</a><a href="#">Sign in</a><a href="#">How it works</a><a href="#">Discover a project</a><a href="#">The baron blog</a><a href="#">Find out more</a>
  </nav>
</header>

<section class="hero">
  <div class="hero-photo" role="img" aria-label="Close-up of stacked coins topped with small green model houses"></div>
  <div class="hero-caption">
    <h1>One property at a time</h1>
    <p>Invest from 1% in a property. Diversify across cities and properties.</p>
  </div>
  <a class="hero-arrow prev" href="#"><svg width="14" height="14" viewBox="0 0 14 14"><polyline points="9,2 4,7 9,12" fill="none" stroke="#fff" stroke-width="2"/></svg></a>
  <a class="hero-arrow next" href="#"><svg width="14" height="14" viewBox="0 0 14 14"><polyline points="5,2 10,7 5,12" fill="none" stroke="#fff" stroke-width="2"/></svg></a>
  <div class="hero-dots"><span class="on"></span><span></span><span></span><span></span></div>
</section>

<section class="intro">
  <h2 class="section-title">Social real estate investment</h2>
  <div class="rule"></div>
  <p>By harnessing the power of crowds, it's possible to become a landlord in locations around the world. Forget the burden of<br>financing <span class="green">100%</span> of the purchase.</p>
  <p>Leave the day to day management of your property portfolio to us.</p>
  <p>Start with <span class="green">1%</span> in a project and plan your steps to becoming a true baron</p>
</section>

<section class="actions">
  <div class="action">
    <div class="action-card">
      <div class="action-icon" role="img" aria-label="Icon of city buildings"></div>
      <div><h2>Find properties</h2><p>Sign up to browse the portfolio.<br>Your journey to becoming a real<br>estate baron starts here.</p></div>
    </div>
    <a class="action-btn" href="#">Become a member</a>
  </div>
  <div class="action">
    <div class="action-card">
      <div class="action-icon" role="img" aria-label="Icon of a group of investors"></div>
      <div><h2>Find Buyers</h2><p>Submit a property or development<br>and raise funds from our real estate<br>barons.</p></div>
    </div>
    <a class="action-btn" href="#">Submit a property</a>
  </div>
</section>

<section class="projects">
  <h2 class="section-title">Featured Projects</h2>
  <p class="projects-lead">Brief details of new and popular projects. To view full listings, you will be required to<br>sign up and <span class="green">become a member.</span></p>
  <div class="project-grid">
    <article class="project raised">
      <div class="project-photo photo-a" role="img" aria-label="Red brick family house with double garage">
        <span class="price-tag">From GBP 3,600</span><span class="launch-tag">New Launch</span>
      </div>
      <div class="project-body">
        <h3>14 Harbour Row LONDON E1</h3>
        <p>Lorem Ipsum is simply dummy text of the printing and typesetting industry. Lorem Ipsum has been the industry's...</p>
        <div class="funded">Funded<div class="bar"><div class="bar-fill" style="width:50%"></div><span class="bar-value">50%</span></div></div>
        <a class="project-link active" href="#">See Project Details</a>
      </div>
    </article>
    <article class="project">
      <div class="project-photo photo-b" role="img" aria-label="Suburban two-storey house with white garage">
        <span class="price-tag">From GBP 3,600</span><span class="launch-tag">New Launch</span>
      </div>
      <div class="project-body">
        <h3>14 Harbour Row LONDON E1</h3>
        <p>Lorem Ipsum is simply dummy text of the printing and typesetting industry. Lorem Ipsum has been the industry's...</p>
        <div class="funded">Funded<div class="bar"><div class="bar-fill" style="width:75%"></div><span class="bar-value">75%</span></div></div>
        <a class="project-link" href="#">See Project Details</a>
      </div>
    </article>
    <article class="project">
      <div class="project-photo photo-c" role="img" aria-label="Mediterranean villa with terracotta roof and palm trees">
        <span class="price-tag">From GBP 3,600</span><span class="launch-tag">New Launch</span>
      </div>
      <div class="project-body">
        <h3>14 Harbour Row LONDON E1</h3>
        <p>Lorem Ipsum is simply dummy text of the printing and typesetting industry. Lorem Ipsum has been the industry's...</p>
        <div class="funded">Funded<div class="bar"><div class="bar-fill" style="width:40%"></div><span class="bar-value">40%</span></div></div>
        <a class="project-link" href="#">See Project Details</a>
      </div>
    </article>
  </div>
</section>

<section class="community">
  <div class="community-photo" role="img" aria-label="Dimmed black and white city skyline at dusk"></div>
  <div class="community-inner">
    <h2 class="section-title">Be Part of a Growing International Community</h2>
    <p class="community-lead">Gain access to new projects in world class cities and join our growing community of international landlords.</p>
    <div class="stats">
      <div class="stat">
        <div class="stat-map" role="img" aria-label="World map with location pins"></div>
        <div class="stat-figure">3,200 barons<br>in 6 countries</div>
        <p class="stat-note">A community of international<br>property barons.</p>
      </div>
      <div class="stat">
        <div class="stat-map" role="img" aria-label="Group of people icon"></div>
        <div class="stat-figure">USD$ 16.2 million</div>
        <p class="stat-note">Collective buying power of<br>the pebblemarquis community</p>
      </div>
      <div class="stat">
        <div class="stat-map" role="img" aria-label="World map with location pins"></div>
        <div class="stat-figure">64 proposals in 6<br>countries</div>
        <p class="stat-note">Attractive real estate from<br>around the world</p>
      </div>
    </div>
  </div>
</section>

<section class="press">
  <div class="press-box">
    <div class="press-row first">
      <span class="press-badge dark" style="width:110px"></span>
      <span class="press-badge dark" style="width:128px"></span>
      <span class="press-badge dark" style="width:70px"></span>
      <span class="press-badge dark" style="width:240px"></span>
    </div>
    <div class="press-row second">
      <span class="press-badge" style="width:56px"></span>
      <span class="press-badge dark" style="width:100px"></span>
      <span class="press-badge dark" style="width:40px;height:34px"></span>
      <span class="press-badge dark" style="width:70px;height:34px"></span>
      <span class="press-badge" style="width:140px"></span>
    </div>
  </div>
  <div class="press-tag">Featured In</div>
</section>

<div class="skyline" role="img" aria-label="Grey silhouette of world landmarks and city skylines"></div>

<div class="footer-bar">
  <div class="footer-follow">Follow us on <span class="social-outline"></span><span class="social-outline"></span></div>
  <span class="copyright">© pebblemarquis 2014</span>
</div>

<footer class="site-footer">
  <div class="footer-top">
    <p><span class="green">Pebble Marquis</span> is part of the Larchfield Capital Group. The Larchfield Capital Group is a worldwide pioneer and leader in the crowd investing, peer to peer and online investment market.</p>
    <span class="group-name">Larchfield Capital Group</span>
  </div>
  <p class="legal">By accessing this site and any pages thereof, you agree to be bound by the terms and conditions. This website is only suitable, intended and available for professional or sophisticated, or similar investors in other jurisdictions, or those who are members of pebblemarquis community and familiar with, and willing to, accept the risks associated with private participation. Pebblemarquis does not endorse any of the projects that appear on this website, nor does it make any recommendations regarding the appropriateness of particular opportunities for any participant. Each potential participant must review and evaluate the projects in his or her own discretion and determine the suitability of participating.</p>
  <p class="legal">This website (the "Site") is in every respect unaffiliated with any site to which it links or to any company or entity (and connected projects, investment opportunity or similar) featured on this Site, and is not meant as an endorsement of any of those companies or entities ("third parties"). Furthermore and for the avoidance of doubt, Pebblemarquis Limited is in no way affiliated with any third parties featured or referenced on this Site. There is no commercial relationship between Pebblemarquis Limited and such third parties, nor an agency arrangement or similar. If you believe your Content (including third party content) as each such term is defined in our Terms of Service has been reproduced on the Site without permission, please refer to our Terms of Service for information on how to request its removal from the Site.</p>
</footer>

</body>
</html>
```